Calvoterra business card

a nice business card with the logo,
Calvoterra
Teresa Lindqvist
Marketing Director
CH-1563 Geneva
Switzerland
+41 76 382 1904
email: Teresa.Lindqvist@calvoterra-mail.example

Target Market(s)

fertilizer business people, very nice and classic business card, normal size, make it nice and funky, try to make it different from the normal boring ones if possible.

Industry/Entity Type

Farming

Number of Pages Required

1 page

Requirements
Must have
• logo, Calvoterra, my name - mail and phone number
regular business card size for me to print easy please

```html
<!DOCTYPE html>
<html lang="en">
<head>
<meta charset="utf-8">
<title>Calvoterra – Teresa Lindqvist business card</title>
<link rel="stylesheet" href="https://fonts.googleapis.com/css2?family=Arimo&family=Great+Vibes&family=Playfair+Display:ital,wght@1,700&display=swap">
<style>
  :root {
    --sun-yellow: #fff200;
    --lime: #b5d334;
    --leaf-green: #2bb24c;
    --harvest-orange: #e9b04b;
    --pale-cream: #f6f7e4;
    --wave-yellow: #ffe94a;
    --field-gold: #e8cf47;
    --meadow-green: #a9d36a;
    --wordmark-grey: #8c8c8c;
    --ink: #1d1d1b;
  }
  html, body {
    margin: 0;
    padding: 0;
    overflow: hidden;
    background: #ffffff;
  }
  .card {
    position: relative;
    width: 1200px;
    height: 686px;
    overflow: hidden;
    background: linear-gradient(90deg,
      var(--sun-yellow) 0%,
      var(--lime) 24%,
      #74c043 40%,
      var(--leaf-green) 52%,
      #8fb24a 68%,
      var(--harvest-orange) 100%);
  }
  .card__art {
    position: absolute;
    inset: 0;
    width: 1200px;
    height: 686px;
  }
  .brand {
    position: absolute;
    left: 6px;
    top: 322px;
    margin: 0;
    font-family: "Arimo", Arial, sans-serif;
    font-weight: 400;
    font-size: 24px;
    letter-spacing: 15px;
    color: var(--wordmark-grey);
    text-transform: uppercase;
  }
  .person__name {
    position: absolute;
    left: 636px;
    top: 66px;
    margin: 0;
    font-family: "Great Vibes", cursive;
    font-weight: 400;
    font-size: 46px;
    line-height: 1;
    color: var(--ink);
  }
  .person__role {
    position: absolute;
    left: 727px;
    top: 114px;
    margin: 0;
    font-family: "Playfair Display", Georgia, serif;
    font-style: italic;
    font-weight: 700;
    font-size: 28px;
    line-height: 1;
    color: var(--ink);
  }
  .contact {
    position: absolute;
    left: 673px;
    top: 172px;
    margin: 0;
    font-family: "Arimo", Arial, sans-serif;
    font-size: 30px;
    line-height: 1;
    color: var(--ink);
  }
  .contact__line {
    position: absolute;
    left: 0;
    white-space: nowrap;
  }
  .contact__line--label-address { top: 0; }
  .contact__line--street { top: 40px; }
  .contact__line--country { top: 80px; }
  .contact__line--label-phone { top: 109px; }
  .contact__line--phone { top: 150px; left: 9px; }
  .contact__line--label-email { top: 190px; }
  .contact__line--email { top: 232px; font-size: 23px; }
</style>
</head>
<body>
  <main class="card">
    <svg class="card__art" viewBox="0 0 1200 686" aria-hidden="false">
      <rect class="top-texture" x="0" y="0" width="1200" height="120" fill="#ffffff" opacity="0.12" role="img" aria-label="Faint diagonal stripe texture across the top band"></rect>
      <path class="wave-cream" d="M0 458 C230 372 460 362 700 420 S1000 558 1200 556 L1200 686 L0 686 Z" fill="var(--pale-cream)" opacity="0.85"></path>
      <path class="wave-yellow" d="M0 470 C230 390 470 380 710 438 S1010 574 1200 572 L1200 686 L0 686 Z" fill="var(--wave-yellow)"></path>
      <path class="field-texture" d="M0 480 C230 402 470 394 710 452 S1010 592 1200 592 L1200 686 L0 686 Z" fill="var(--field-gold)" role="img" aria-label="Diagonal stripe texture in soft gold and green tones"></path>
      <path class="meadow-band" d="M0 618 C400 612 800 640 1200 650 L1200 686 L0 686 Z" fill="var(--meadow-green)" opacity="0.9"></path>
    </svg>

    <p class="brand">Calvoterra</p>

    <h1 class="person__name">Teresa Lindqvist</h1>
    <p class="person__role">Marketing Director</p>

    <address class="contact">
      <span class="contact__line contact__line--label-address">Address:</span>
      <span class="contact__line contact__line--street">CH-1563 Geneva</span>
      <span class="contact__line contact__line--country">Switzerland</span>
      <span class="contact__line contact__line--label-phone">Phone:</span>
      <span class="contact__line contact__line--phone">+41 76 382 1904</span>
      <span class="contact__line contact__line--label-email">Email:</span>
      <span class="contact__line contact__line--email">Teresa.Lindqvist@calvoterra-mail.example</span>
    </address>
  </main>
</body>
</html>
```